Bright Ledger Works! - Business cards

Greetings -

Please design a business card complementary to the attached POSTCARD. We are open to 1) design leveraging POSTCARD that can also be integrated into complementary website; OR 2) totally new design, new colors that communicate what we do: ...

We provide administrative support services to small businesses and executives.

The cards will be presented to depts, such as: 1) retail print services, 2) concierge desks, 3) coffee shop entrepreneurs and patrons...both end users and those who refer to us. Simple, uncluttered design is preferred. (The back of OLD business card attached provided list of services.)

Feel free to request more information.

Target Market(s)

small businesses and executives
The cards will be presented to depts, such as: 1) retail print services, 2) concierge desks, 3) coffee shop entrepreneurs and patrons...both end users and those who refer to us

Industry/Entity Type

Business

Contact Information for Business Card

See POSTCARD

Font styles to use
Serif
Sans Serif

Colors
f04a50
3276b5
fbee3d
faa54b
acd036

Requirements
Must have
• Simple, uncluttered design

```html
<!DOCTYPE html>
<html lang="en">
<head>
<meta charset="utf-8">
<title>Bright Ledger Works! – Business Cards</title>
<link rel="stylesheet" href="https://fonts.googleapis.com/css2?family=Source+Sans+3:wght@400;600;700;800&display=swap">
<style>
  :root {
    --stage: #e9e6e0;
    --card-dark: #2e2c22;
    --paper: #ffffff;
    --olive: #b5bd32;
    --white: #ffffff;
    --tile-green: #2f5014;
    --tile-brown: #8a3a17;
    --tile-teal: #2d5e55;
    --tile-orange: #f0561c;
    --tile-red: #e8141e;
    --tile-olive: #b8b93a;
    --shadow: 0 3px 8px rgba(0,0,0,.28);
  }
  * { box-sizing: border-box; margin: 0; padding: 0; }
  html, body { width: 1200px; height: 900px; overflow: hidden; }
  body {
    background: var(--stage);
    font-family: "Source Sans 3", "Helvetica Neue", Arial, sans-serif;
    position: relative;
  }
  .card { position: absolute; box-shadow: var(--shadow); overflow: hidden; }

  /* Front */
  .card-front { left: 320px; top: 88px; width: 580px; height: 357px; background: var(--card-dark); color: var(--white); }
  .brand-name {
    position: absolute; top: 72px; left: 0; width: 100%; text-align: center;
    font-size: 38px; font-weight: 800; color: var(--white); letter-spacing: -.5px;
  }
  .contact { position: absolute; top: 166px; left: 0; width: 100%; }
  .person { position: absolute; right: 295px; text-align: right; }
  .person-name { font-size: 20px; font-weight: 600; color: var(--olive); line-height: 26px; }
  .person-title { font-size: 17px; line-height: 26px; }
  .details { position: absolute; left: 305px; font-size: 17px; line-height: 26px; }
  .details b { color: var(--olive); font-weight: 700; margin-right: 4px; }
  .tagline {
    position: absolute; top: 268px; left: 0; width: 100%; text-align: center;
    font-size: 22px; font-weight: 600; color: var(--olive);
  }

  /* Back */
  .card-back { left: 320px; top: 478px; width: 583px; height: 359px; background: var(--paper); }
  .back-field { position: absolute; inset: 0; }
  .back-name {
    position: absolute; left: 345px; top: 175px; transform: translate(-50%,-50%) rotate(-47deg);
    white-space: nowrap; font-size: 40px; font-weight: 800; color: var(--white);
  }
  .service {
    position: absolute; width: 90px; height: 90px; color: var(--white);
    font-size: 13px; font-weight: 600; line-height: 15px; text-align: center;
    padding-top: 12px;
  }
  .service svg { position: absolute; left: 33px; top: 52px; width: 24px; height: 24px; }
  .presentations { left: 483px; top: 43px; background: var(--tile-green); padding-top: 20px; }
  .travel { left: 387px; top: 139px; background: var(--tile-brown); }
  .research { left: 483px; top: 139px; background: var(--tile-teal); }
  .billing { left: 292px; top: 235px; background: var(--tile-orange); }
  .resumes { left: 388px; top: 235px; background: var(--tile-red); padding-top: 16px; }
  .meeting { left: 483px; top: 235px; background: var(--tile-olive); }
</style>
</head>
<body>

<section class="card card-front">
  <h1 class="brand-name">Bright Ledger Works!</h1>
  <div class="contact">
    <div class="person">
      <div class="person-name">R. K. DALTON</div>
      <div class="person-title">Director / Systems Engineer</div>
    </div>
    <div class="details">
      <div><b>P:</b>(312) 555-0148</div>
      <div><b>E:</b>rk.dalton@brightledger.net</div>
    </div>
  </div>
  <p class="tagline">BUSINESS SUPPORT SERVICES</p>
</section>

<section class="card card-back">
  <svg class="back-field" viewBox="0 0 583 359" width="583" height="359" aria-hidden="true">
    <polygon points="0,0 462,0 120,359 0,359" fill="var(--card-dark)"/>
  </svg>
  <div class="back-name">Bright Ledger Works!</div>

  <div class="service presentations">Presentations
    <svg viewBox="0 0 24 24" fill="none" stroke="#c9c9a0" stroke-width="1.6"><rect x="3" y="4" width="18" height="12"/><path d="M12 16v5M8 21l4-5 4 5"/><path d="M6 8h5M6 11h4"/></svg>
  </div>
  <div class="service travel">Travel Arrangements
    <svg viewBox="0 0 24 24" fill="none" stroke="#d9a78c" stroke-width="1.6"><rect x="6" y="6" width="12" height="15" rx="2"/><path d="M10 6V3h4v3M9 21v2M15 21v2"/></svg>
  </div>
  <div class="service research">Industry Research
    <svg viewBox="0 0 24 24" fill="#fff"><circle cx="5" cy="6" r="2.2"/><circle cx="12" cy="5" r="2.2"/><circle cx="19" cy="6" r="2.2"/><rect x="3" y="9" width="4" height="7"/><rect x="10" y="8" width="4" height="8"/><rect x="17" y="9" width="4" height="7"/><rect x="2" y="16" width="20" height="2"/><rect x="6" y="18" width="2" height="5"/><rect x="16" y="18" width="2" height="5"/></svg>
  </div>
  <div class="service billing">Client Billing
    <svg viewBox="0 0 24 24" fill="#fff"><circle cx="5" cy="6" r="2.2"/><circle cx="12" cy="5" r="2.2"/><circle cx="19" cy="6" r="2.2"/><rect x="3" y="9" width="4" height="7"/><rect x="10" y="8" width="4" height="8"/><rect x="17" y="9" width="4" height="7"/><rect x="2" y="16" width="20" height="2"/><rect x="6" y="18" width="2" height="5"/><rect x="16" y="18" width="2" height="5"/></svg>
  </div>
  <div class="service resumes">Resumes
    <svg viewBox="0 0 24 24" fill="none" stroke="#f4c0c0" stroke-width="1.6"><rect x="5" y="3" width="14" height="18"/><path d="M8 8h8M8 12h8M8 16h5"/></svg>
  </div>
  <div class="service meeting">Meeting planning
    <svg viewBox="0 0 24 24" fill="#fff"><circle cx="5" cy="6" r="2.2"/><circle cx="12" cy="5" r="2.2"/><circle cx="19" cy="6" r="2.2"/><rect x="3" y="9" width="4" height="7"/><rect x="10" y="8" width="4" height="8"/><rect x="17" y="9" width="4" height="7"/><rect x="2" y="16" width="20" height="2"/><rect x="6" y="18" width="2" height="5"/><rect x="16" y="18" width="2" height="5"/></svg>
  </div>
</section>

</body>
</html>
```